Business card and logo designs

We are looking to create a cool and trendy image for the company, some thing what quince has. We already have a logo, but we can reconsider a new logo.

Volturo provides a new kind of web service for businesses to take appointments using web and mobile. Usually a customer needs to call or check several times. Volturo solves this trouble. Our service refills cancellations quickly and automatically plus reduces no-shows. On top of that, our analytical tools give deep business and customer insights to increase revenue.

Phone bookings and cancellations are frustrating, time-consuming and expensive.It can take hours to book a 20 min appointment for e.g. with your doctor. When customers don’t find a suitable time, they need to call or check online again and again. Volturo turn the tables and enables your doctor to get back to you with appointment of your choice,automatically. It refills cancellations quickly and automatically. Volutro did not invent a booking system, like Quince did not invest a mobile phone. However, we make it mobile, intelligent and useful.

Volturo identity should present a change, the same one which quince brought to mobile. Despite the fact that booking systems has been around for 2 decades, we change the game.

We want to communicate that we are saving time for consumers and businesses in an an innovative way and helping businesses to improve revenue.
Updates

Reason: We want more design entries.

Contents of the business card....

But we want the empty template so when new people join, we use the same.

Tomas Lindqvel

+358-402759130

Founder & CEO 

tomas.lindqvel@volturo.example

 Volturo Solutions Oy

Kallvik, Norrmark

www.volturo.example

All,

We have to get ideas about a new logo. New business card is not enough.

Reason: More designs needed...

Reason: We have got very few good designs so far.

Reason: Need a bite more time... our creative director was busy

Target Market(s)

Most developed countries

Industry/Entity Type

Doctor

Requirements
Must have
• Color orange and green....
Should not have
• Should not have the obvious things... more intelligent design...

```html
<!DOCTYPE html>
<html lang="en">
<head>
<meta charset="utf-8">
<title>Volturo Business Card</title>
<link rel="stylesheet" href="https://fonts.googleapis.com/css2?family=Source+Sans+3:ital,wght@0,400;0,600;1,400&display=swap">
<style>
  :root {
    --backdrop: #141414;
    --card-light: #ffffff;
    --card-shade: #e9e9e9;
    --brand-orange: #f26a1b;
    --ink-dark: #2b2b2b;
    --ink-grey: #6a6a6a;
    --ink-faint: #c4c4c4;
    --rule: #8f8f8f;
  }
  * { margin: 0; padding: 0; box-sizing: border-box; }
  html, body {
    width: 1200px;
    height: 815px;
    overflow: hidden;
    background: var(--backdrop);
    font-family: "Source Sans 3", "Myriad Pro", Arial, sans-serif;
  }
  .stage {
    position: relative;
    width: 1200px;
    height: 815px;
  }
  .business-card {
    position: absolute;
    left: 170px;
    top: 155px;
    width: 816px;
    height: 478px;
    background: radial-gradient(ellipse at 35% 30%, var(--card-light) 0%, #f6f6f6 45%, var(--card-shade) 100%);
  }
  .brand-lockup {
    position: absolute;
    right: 96px;
    top: 42px;
    text-align: right;
  }
  .brand-name {
    display: flex;
    align-items: center;
    justify-content: flex-end;
    gap: 8px;
    font-size: 44px;
    font-weight: 600;
    line-height: 1;
    letter-spacing: -0.5px;
    color: var(--ink-dark);
  }
  .brand-dot {
    width: 14px;
    height: 14px;
    border-radius: 50%;
    background: var(--brand-orange);
  }
  .brand-tagline {
    margin-top: 4px;
    font-size: 16px;
    letter-spacing: 0.6px;
    color: var(--ink-grey);
  }
  .holder-name {
    position: absolute;
    right: 108px;
    top: 124px;
    font-size: 25px;
    font-style: italic;
    color: var(--brand-orange);
    letter-spacing: 0.3px;
    white-space: nowrap;
  }
  .divider {
    position: absolute;
    left: 56px;
    top: 212px;
    width: 714px;
    height: 1px;
    background: var(--rule);
  }
  .contact {
    position: absolute;
    left: 57px;
    font-size: 17px;
    line-height: 19px;
    letter-spacing: -0.8px;
    text-transform: uppercase;
    white-space: nowrap;
  }
  .contact-web { top: 235px; color: var(--brand-orange); }
  .contact-details { top: 291px; }
  .contact-details .primary { color: var(--brand-orange); }
  .contact-details .secondary { color: var(--ink-faint); }
</style>
</head>
<body>
<main class="stage">
  <section class="business-card">
    <div class="brand-lockup">
      <div class="brand-name"><span class="brand-dot"></span>volturo</div>
      <div class="brand-tagline">timely appointments</div>
    </div>
    <div class="holder-name">TOMAS LINDQVEL</div>
    <div class="divider"></div>
    <div class="contact contact-web">www.volturo.example</div>
    <div class="contact contact-details">
      <div class="primary">Volturo Solutions Oy</div>
      <div class="primary">Kallvik, Norrmark</div>
      <div class="primary">tomas.lindqvel@volturo.example</div>
      <div class="secondary">+358-402759130</div>
      <div class="secondary">(555) 555 - 6789 (Work)</div>
      <div class="secondary">(555) 555 - 1234 (Cell)</div>
    </div>
  </section>
</main>
</body>
</html>
```